agricultural technology company needs business cards*

design a business card that represents our business well. please see our website: vastrelbyfieldseal.com.au
professional, simple, clean lines, not complicated or floral.....

```html
<!DOCTYPE html>
<html lang="en">
<head>
<meta charset="utf-8">
<title>Vastrelby FieldSeal – Business Card</title>
<link rel="stylesheet" href="https://fonts.googleapis.com/css2?family=Poppins:wght@400;500;700&family=Allura&display=swap">
<style>
  :root {
    --stage: #1f1f1f;
    --navy: #1f3566;
    --navy-text: #1d2a55;
    --green: #23b14d;
    --lime: #9fcc3b;
    --white: #ffffff;
    --silver: #c7cad1;
  }
  * { margin: 0; padding: 0; box-sizing: border-box; }
  html, body { width: 1200px; height: 1200px; overflow: hidden; }
  body {
    background: var(--stage);
    font-family: "Poppins", sans-serif;
    display: flex;
    flex-direction: column;
    align-items: center;
    justify-content: center;
    gap: 48px;
  }
  .card {
    width: 900px;
    height: 514px;
    position: relative;
    overflow: hidden;
  }
  .card-front {
    background: var(--navy);
    display: flex;
    align-items: center;
    justify-content: center;
  }
  .brand-name {
    font-weight: 700;
    letter-spacing: -0.5px;
    line-height: 0.95;
  }
  .card-front .brand-name {
    color: var(--silver);
    font-size: 64px;
  }
  .card-back { background: var(--white); }
  .brand-block {
    position: absolute;
    left: 70px;
    top: 180px;
    width: 380px;
    color: var(--navy-text);
    font-size: 58px;
  }
  .divider {
    position: absolute;
    left: 474px;
    top: 120px;
    width: 1.5px;
    height: 250px;
    background: var(--navy-text);
  }
  .contact {
    position: absolute;
    left: 510px;
    top: 112px;
    color: var(--navy-text);
  }
  .person-name {
    font-family: "Allura", cursive;
    color: var(--green);
    font-size: 66px;
    line-height: 1;
  }
  .person-role {
    font-size: 20px;
    font-weight: 500;
    margin: 0 0 18px;
  }
  .contact-list { list-style: none; font-size: 18px; line-height: 1.45; }
  .contact-list li { display: flex; align-items: flex-start; gap: 12px; }
  .contact-list .icon {
    flex: none;
    width: 18px; height: 18px;
    margin-top: 4px;
    background: var(--green);
    border-radius: 2px;
    display: flex; align-items: center; justify-content: center;
  }
  .contact-list .icon svg { width: 12px; height: 12px; }
  .address { padding-left: 0; }
  .colour-band {
    position: absolute;
    left: 0; bottom: 0;
    width: 100%; height: 16px;
    display: flex;
  }
  .colour-band span:nth-child(1) { flex: 40; background: var(--navy-text); }
  .colour-band span:nth-child(2) { flex: 23; background: var(--green); }
  .colour-band span:nth-child(3) { flex: 37; background: var(--lime); }
</style>
</head>
<body>
  <section class="card card-front">
    <div class="brand-name">Vastrelby<br>FieldSeal</div>
  </section>

  <section class="card card-back">
    <div class="brand-block brand-name">Vastrelby<br>FieldSeal</div>
    <div class="divider"></div>
    <div class="contact">
      <p class="person-name">Joren Altveld</p>
      <p class="person-role">Founder &amp; co-owner</p>
      <ul class="contact-list">
        <li><span class="icon"><svg viewBox="0 0 12 12"><path d="M2.5 1.5l2 0 .8 2.2-1.2.9c.6 1.3 1.5 2.2 2.8 2.8l.9-1.2 2.2.8 0 2c0 .6-.5 1-1 1C4.8 10 2 7.2 1.5 2.5c0-.5.4-1 1-1z" fill="#fff"/></svg></span>1300 555 019</li>
        <li><span class="icon"><svg viewBox="0 0 12 12"><rect x="1.5" y="3" width="9" height="6" fill="none" stroke="#fff" stroke-width="1"/><path d="M1.5 3L6 6.5 10.5 3" fill="none" stroke="#fff" stroke-width="1"/></svg></span>info@vastrelbyfieldseal</li>
        <li><span class="icon"><svg viewBox="0 0 12 12"><circle cx="6" cy="6" r="4.2" fill="none" stroke="#fff"/><path d="M1.8 6h8.4M6 1.8c-2 2.4-2 6 0 8.4M6 1.8c2 2.4 2 6 0 8.4" fill="none" stroke="#fff" stroke-width=".8"/></svg></span>vastrelbyfieldseal.com.au</li>
        <li><span class="icon"><svg viewBox="0 0 12 12"><path d="M6 11s-3.5-3.8-3.5-6.2a3.5 3.5 0 0 1 7 0C9.5 7.2 6 11 6 11z" fill="#fff"/><circle cx="6" cy="4.8" r="1.3" fill="#23b14d"/></svg></span><span class="address">14 Harlow Road, Kellerton<br>14 Harlow Rd, 14 Harlow Rd<br>Kellerton WA 6999</span></li>
      </ul>
    </div>
    <div class="colour-band"><span></span><span></span><span></span></div>
  </section>
</body>
</html>
```